" Atualmente somos dois sócios com experiência no mercado financeiro. A empresa foi fundada em 2016 e desde o início nossos escopo de trabalho se resume a captar clientes para processos de fusões e aquisições, seja para venda parcial ou total das empresas de nossos clientes. Desde a criação da empresa concluímos 3 transações importantes, além de diversas assessorias de valuation (avaliação de valor de empresas) e consultoria financeira. "

```html
<!DOCTYPE html>
<html lang="pt-BR">
<head>
<meta charset="utf-8">
<title>Vela Capital — Cartões de visita</title>
<link href="https://fonts.googleapis.com/css2?family=Arimo:wght@400;700&family=Montserrat:wght@500;700&display=swap" rel="stylesheet">
<style>
  :root {
    --backdrop: #dcdcde;
    --card: #f7f7f7;
    --card-fade: #e9e9ea;
    --navy: #1f2a44;
    --gold: #b89a5c;
    --text: #2a2f3a;
  }
  html, body {
    margin: 0;
    width: 1200px;
    height: 1200px;
    overflow: hidden;
    background: var(--backdrop);
  }
  .stack {
    position: absolute;
    left: 336px;
    top: 384px;
    width: 564px;
    display: flex;
    flex-direction: column;
    gap: 18px;
  }
  .card {
    position: relative;
    width: 564px;
    height: 228px;
    background: var(--card);
    box-sizing: border-box;
    padding: 20px 16px 0 16px;
    font-family: "Arimo", Arial, sans-serif;
    color: var(--text);
    overflow: hidden;
  }
  .card__decor {
    position: absolute;
    top: 0;
    right: 0;
    width: 310px;
    height: 100%;
    background: linear-gradient(135deg, var(--card-fade) 0%, #f3f3f4 55%, var(--card) 100%);
  }
  .brand {
    position: relative;
    display: flex;
    align-items: center;
    gap: 10px;
    font-family: "Montserrat", Arial, sans-serif;
    font-weight: 700;
    font-size: 27px;
    letter-spacing: 0.5px;
    color: var(--navy);
  }
  .brand__mark {
    width: 26px;
    height: 26px;
    background: var(--gold);
  }
  .person {
    position: relative;
    margin: 18px 0 14px;
    font-size: 18px;
    font-weight: 700;
    color: var(--navy);
  }
  .contact, .address {
    position: relative;
    margin: 0;
    font-size: 12.5px;
    line-height: 15px;
  }
  .address { margin-top: 8px; }
  .social {
    position: relative;
    display: flex;
    align-items: center;
    gap: 6px;
    margin-top: 9px;
    font-size: 12px;
  }
  .social__dot {
    width: 11px;
    height: 11px;
    border-radius: 50%;
    background: var(--gold);
  }
</style>
</head>
<body>
  <main class="stack">
    <article class="card">
      <div class="card__decor" role="img" aria-label="Faint brand symbol decoration"></div>
      <div class="brand"><span class="brand__mark"></span>VELA CAPITAL</div>
      <div class="person">Rafael Moura Tanaka</div>
      <p class="contact">+55 11 90000-1234<br>rafael.tanaka@velacapital.com.br<br>www.velacapital.com.br</p>
      <p class="address">Rua das Acácias, 820 - Cj. 12<br>CEP 04518-003 - São Paulo SP</p>
      <div class="social"><span class="social__dot"></span>Vela Capital</div>
    </article>
    <article class="card">
      <div class="card__decor" role="img" aria-label="Faint brand symbol decoration"></div>
      <div class="brand"><span class="brand__mark"></span>VELA CAPITAL</div>
      <div class="person">Lucas Ferrante</div>
      <p class="contact">+55 11 90000-5678<br>lucas.ferrante@velacapital.com.br<br>www.velacapital.com.br</p>
      <p class="address">Rua das Acácias, 820 - Cj. 12<br>CEP 04518-003 - São Paulo SP</p>
      <div class="social"><span class="social__dot"></span>Vela Capital</div>
    </article>
  </main>
</body>
</html>
```